seeking a modern Business Card design for Roof Plumbering Business

halbury roof plumbing is a local metal re-roof and new construction specialist. We are seeking a modern business card to assist with networking within the industry. Our services are predominantly the installation of metal roofs on new houses, however we also do re-roofs when an existing roof needs replacing. We service both residential and commercial properties. Please include the below details on the card:
Name: Owen Halbury
Phone: 0481 257 936
Email: owenhalburyroofing@tindlemail.com

Residential & Commercial
Re-roof & New Construction
Fully Insured

I have uploaded our business logo, which we think would suit a black background. Please use all lower case for business name.
Cheers
Updates

Hey Guys, As requested I've uploaded a Pdf version of my logo. Hopefully this help. Thanks

Industry/Entity Type

Business

Contact Information for Business Card

Name: Owen Halbury
Phone: 0481 257 936

Residential & Commercial
Fully Insured

Font styles to use
Serif
Sans Serif

Requirements
Must have
• Name must be all lower case "halbury roof plumbing"
Nice to have
• Stick with Logo Colours

```html
<!DOCTYPE html>
<html lang="en">
<head>
<meta charset="utf-8">
<title>halbury roof plumbing – business card</title>
<link rel="stylesheet" href="https://fonts.googleapis.com/css2?family=Montserrat:wght@400;500;600&display=swap">
<style>
  :root {
    --backdrop: #939393;
    --card: #ffffff;
    --brand-blue: #36a2d6;
    --text-grey: #555555;
    --band-text: #ffffff;
  }
  html, body {
    margin: 0;
    width: 1200px;
    height: 1200px;
    overflow: hidden;
    background: var(--backdrop);
    font-family: "Montserrat", sans-serif;
  }
  .card {
    position: absolute;
    left: 174px;
    top: 363px;
    width: 851px;
    height: 473px;
    background: var(--card);
    overflow: hidden;
  }
  .brand-name {
    position: absolute;
    right: 81px;
    top: 128px;
    margin: 0;
    font-size: 27px;
    font-weight: 500;
    color: var(--brand-blue);
    letter-spacing: 0.5px;
    white-space: nowrap;
  }
  .contact {
    position: absolute;
    left: 80px;
    top: 283px;
  }
  .person-name {
    margin: 0 0 14px;
    font-size: 27px;
    font-weight: 600;
    color: var(--text-grey);
    line-height: 32px;
  }
  .contact-line {
    display: flex;
    align-items: center;
    height: 30px;
    font-size: 20px;
    color: var(--text-grey);
  }
  .contact-line svg {
    width: 22px;
    height: 18px;
    margin-right: 18px;
    fill: none;
    stroke: var(--brand-blue);
    stroke-width: 2;
  }
  .services-band {
    position: absolute;
    left: 0;
    bottom: 0;
    width: 100%;
    height: 49px;
    background: var(--brand-blue);
    color: var(--band-text);
    font-size: 19px;
  }
  .services-band span {
    position: absolute;
    top: 12px;
    white-space: nowrap;
  }
</style>
</head>
<body>
  <div class="card">
    <p class="brand-name">halbury roof plumbing</p>

    <div class="contact">
      <h1 class="person-name">Owen Halbury</h1>
      <div class="contact-line">
        <svg viewBox="0 0 22 18" aria-hidden="true">
          <path d="M2 6 Q11 0 20 6 L18 8 L15 6 L7 6 L4 8 Z" fill="var(--brand-blue)"/>
          <path d="M6 9 L16 9 L19 16 L3 16 Z"/>
          <circle cx="11" cy="12.5" r="2"/>
        </svg>
        0481 257 936
      </div>
      <div class="contact-line">
        <svg viewBox="0 0 22 18" aria-hidden="true">
          <rect x="1" y="2" width="20" height="14"/>
          <path d="M1 2 L11 10 L21 2 M1 16 L8 8 M21 16 L14 8"/>
        </svg>
        owenhalburyroofing@tindlemail.com
      </div>
    </div>

    <div class="services-band">
      <span style="left:81px">Residential &amp; Commercial</span>
      <span style="left:325px">-</span>
      <span style="left:354px">Re-roof &amp; New Construction</span>
      <span style="left:628px">-</span>
      <span style="left:657px">Fully Insured</span>
    </div>
  </div>
</body>
</html>
```